Business card website / business card for website

We are a French website selling products Made in USA of quality, we need a business card to give from hand to hand and for deposit in the cartons of Each order. We-have the logo That I send in the attachments The theme is: US Vintage and find the compromised entre les national park ambience us and the atmosphere Brooklyn If you can make the feeling it's great The site www.latablederivebleue.com (opening April) You can change the logo a little gold in color it could ... we are a French website selling products Made in USA quality, we need a business card to give from hand to hand and deposit in cartons each order. we have the logo that I convey in the attached parts is the theme: Vintage embiance US and find a compromise between the atmosphere us national park and the atmosphere Brooklyn at: www.latablederivebleue.com (opening April) if you can the impression is great

Target Market(s)

25-50 YEARS man, woman.

Industry/Entity Type

Business

Contact Information for Business Card

www.latablederivebleue.com
N'oubliez pas que nous sommes là si vous avez besoin de nouscontact@latablederivebleue.com

Font styles to use
Serif

Requirements
Must have
• my logo with "general store", my email address preceded by the phrase: Do not forget that we are here if you need us My logo with the words "general store," my email address Preceded by the sentence: remember we're here if you need us (in french)
Nice to have
• i like this style: http://designcorbel.net/ideas/print-ideas/25-charming-old-style-business-card-designs/ must feel the Vintage America it must feel the Vintage America lice can change a little logo or to color ... You can change the logo a little gold in color it could ... i like kraft paper with red ....
Should not have

```html
<!DOCTYPE html>
<html lang="fr">
<head>
<meta charset="utf-8">
<title>La Table de Rive Bleue – General Store business card</title>
<link href="https://fonts.googleapis.com/css2?family=Open+Sans:wght@400;600&display=swap" rel="stylesheet">
<style>
  :root {
    --stage: #000000;
    --paper: #ededed;
    --band: #3b3b3b;
    --ink: #1c1c1c;
    --back: #2f2f2f;
    --back-art: #3a3a3a;
    --seal-light: #dcdcdc;
    --seal-dark: #444444;
  }
  * { margin: 0; padding: 0; box-sizing: border-box; }
  html, body { width: 1200px; height: 900px; overflow: hidden; background: var(--stage); }
  body { position: relative; font-family: "Open Sans", Arial, sans-serif; color: var(--ink); }

  .card {
    position: absolute;
    top: 275px;
    width: 476px;
    height: 293px;
    overflow: hidden;
    box-shadow: 0 4px 10px rgba(255,255,255,0.06);
  }
  .card-front {
    left: 116px;
    background: var(--paper);
    border-radius: 0 46px 0 46px;
  }
  .card-back {
    left: 622px;
    background: var(--back);
    border-radius: 46px 0 46px 0;
  }

  .front-band {
    position: absolute;
    left: 20px; top: 0;
    width: 121px; height: 100%;
    background: var(--band);
  }
  .seal {
    position: absolute;
    border-radius: 50%;
    display: flex;
    align-items: center;
    justify-content: center;
    text-align: center;
    font-weight: 600;
    text-transform: uppercase;
    letter-spacing: 0.5px;
  }
  .seal-front {
    left: 18px; top: 45px;
    width: 124px; height: 124px;
    background: var(--seal-light);
    border: 3px solid #ffffff;
    color: var(--ink);
    font-size: 12px;
    line-height: 1.3;
    padding: 0 14px;
  }
  .store-title {
    position: absolute;
    left: 156px; top: 94px;
    font-size: 22px;
    font-weight: 600;
    letter-spacing: 0.3px;
  }
  .contact {
    position: absolute;
    left: 149px; top: 169px;
    width: 300px;
    font-size: 12.5px;
    line-height: 18px;
  }
  .contact-line {
    display: flex;
    align-items: center;
    gap: 5px;
    margin-top: 3px;
  }
  .contact-line svg { width: 9px; height: 9px; flex: none; }

  .back-art {
    position: absolute;
    inset: 0;
    background: linear-gradient(160deg, var(--back-art) 0%, var(--back) 70%);
  }
  .seal-back {
    left: 163px; top: 83px;
    width: 150px; height: 150px;
    background: var(--seal-dark);
    border: 2px solid #5a5a5a;
    color: #c9c9c9;
    font-size: 13px;
    line-height: 1.35;
    padding: 0 20px;
  }
</style>
</head>
<body>

<section class="card card-front">
  <div class="front-band"></div>
  <div class="seal seal-front">La Table de Rive Bleue</div>
  <h1 class="store-title">GENERAL STORE</h1>
  <div class="contact">
    <p class="contact-intro">N'oubliez pas que nous sommes là si vous avez besoin de</p>
    <p class="contact-line">
      <svg viewBox="0 0 10 10" aria-hidden="true"><rect x="0.5" y="2" width="9" height="6.5" fill="#1c1c1c"/><path d="M0.5 2 L5 5.5 L9.5 2" stroke="#ededed" stroke-width="0.9" fill="none"/></svg>
      nouscontact@latablederivebleue.com
    </p>
    <p class="contact-line">
      <svg viewBox="0 0 10 10" aria-hidden="true"><circle cx="5" cy="5" r="4.5" fill="#1c1c1c"/></svg>
      www.latablederivebleue.com
    </p>
  </div>
</section>

<section class="card card-back">
  <div class="back-art" role="img" aria-label="Embossed line illustration of an old barn with pine trees"></div>
  <div class="seal seal-back">La Table de Rive Bleue</div>
</section>

</body>
</html>
```